Asia based real estate financing firm needs and AWESOME design for a biz card -Harbor Lending Circle

Looking for a stylish, & corporate-looking business card for a real estate financing brokerage firm in Asia, offering global mortgage loans. I uploaded our current logos. We would like to add a splash of color (perhaps the house icon) or any other suggestions are open. For the winning designer, we have a lot of work! Thanks and best of luck!

Target Market(s)

Real estate investors globally. We want to look more like a BANK and NOT a real estate company. Please don't play up on a "house" design.

Industry/Entity Type

Banking

Contact Information for Business Card

Harbor Lending Circle
Peter Wilks
Co-Founder | Partner

14 Cassia Lane, Suite 310
Singapore 047219
www.hlc-example.asia
peterwilks@hlc-example.asia
+65 555-0142
WeChat: peterwilks

Colors

Designer to choose colors to be used in the design.

Requirements
Must have
• Must have the standard business requirements for a card; name, address, email, etc
• Can be horizontal or vertical.
Nice to have
• It would be great to see some sort of variation to the logo with a pop of color. Red is good as we're in Asia, however, other options work as well.
• Our tag line is - Lending beyond borders. It doesn't have to be on the card but might be nice.
• I'd like to start seeing our tagline within the cards as well. - Lending beyond borders.
• Also, please add our location. The location for this card is Singapore so perhaps it can be highlighted or emphasised in some way.
• Singapore | Hong Kong | Shanghai | Manila
• As we will soon open an office in Shanghai, having an option for both languages would be great.
Should not have
• I'm exceited and open to your creativity ... knock it out of the park!

```html
<!DOCTYPE html>
<html lang="en">
<head>
<meta charset="utf-8">
<title>Harbor Lending Circle – Business Card</title>
<link rel="stylesheet" href="https://fonts.googleapis.com/css2?family=Cormorant+Garamond:wght@500&family=Open+Sans:wght@400;700&family=Arimo:ital,wght@1,700&display=swap">
<style>
  :root {
    --backdrop: #1d1d1f;
    --brand-red: #ec1c24;
    --paper: #ffffff;
    --ink: #1a1a1a;
    --serif: "Cormorant Garamond", Georgia, serif;
    --sans: "Open Sans", Arial, sans-serif;
    --tag: "Arimo", Arial, sans-serif;
  }
  * { box-sizing: border-box; margin: 0; padding: 0; }
  html, body { width: 1200px; height: 900px; overflow: hidden; }
  body { background: var(--backdrop); position: relative; }

  .card {
    position: absolute;
    width: 520px;
    height: 300px;
    background: var(--brand-red);
    overflow: hidden;
    box-shadow: 0 14px 30px rgba(0,0,0,.55);
  }
  .card--contact { left: 90px; top: 110px; }
  .card--front { left: 590px; top: 480px; }

  .card__shape { position: absolute; inset: 0; }

  /* Contact side */
  .wordmark {
    position: absolute;
    color: var(--paper);
    font-family: var(--serif);
    font-weight: 500;
    text-transform: uppercase;
    line-height: 1.05;
  }
  .card--contact .wordmark {
    left: 28px; top: 30px;
    font-size: 21px;
    letter-spacing: 1.5px;
  }
  .holder { position: absolute; left: 40px; top: 222px; font-family: var(--sans); }
  .holder__name { color: var(--brand-red); font-weight: 700; font-size: 19px; line-height: 1.2; }
  .holder__role { color: var(--ink); font-size: 12px; }

  .contact {
    position: absolute;
    left: 250px; top: 110px;
    font-family: var(--serif);
    font-weight: 500;
    font-size: 12.5px;
    color: var(--ink);
    border-collapse: collapse;
  }
  .contact th { text-align: left; font-weight: 500; padding: 0 8px 1px 0; vertical-align: top; }
  .contact td { padding: 0 0 1px 0; }

  /* Front side */
  .card--front .wordmark {
    left: 0; right: 0; top: 52px;
    text-align: center;
    font-size: 40px;
    letter-spacing: 3px;
  }
  .tagline {
    position: absolute;
    left: 0; right: 0; top: 222px;
    text-align: center;
    font-family: var(--tag);
    font-style: italic;
    font-weight: 700;
    font-size: 17px;
    color: var(--brand-red);
  }
</style>
</head>
<body>

  <section class="card card--contact" aria-label="Business card, contact side">
    <svg class="card__shape" width="520" height="300" viewBox="0 0 520 300" aria-hidden="true">
      <polygon points="0,232 372,30 455,30 520,58 520,300 0,300" fill="var(--paper)"/>
    </svg>
    <div class="wordmark">Harbor<br>Lending Circle</div>
    <div class="holder">
      <p class="holder__name">Peter Wilks</p>
      <p class="holder__role">Co-Founder | Partner</p>
    </div>
    <table class="contact">
      <tr><th>Address</th><td>: 14 Cassia Lane, Suite 310<br>&nbsp;&nbsp;Singapore 047219</td></tr>
      <tr><th>Website</th><td>: www.hlc-example.asia</td></tr>
      <tr><th>Email</th><td>: peterwilks@hlc-example.asia</td></tr>
      <tr><th>Phone</th><td>: +65 555-0142</td></tr>
      <tr><th>WeChat</th><td>: peterwilks</td></tr>
    </table>
  </section>

  <section class="card card--front" aria-label="Business card, front side">
    <svg class="card__shape" width="520" height="300" viewBox="0 0 520 300" aria-hidden="true">
      <rect x="0" y="208" width="520" height="64" fill="var(--paper)"/>
    </svg>
    <div class="wordmark">Harbor<br>Lending Circle</div>
    <p class="tagline">“Lending beyond borders”</p>
  </section>

</body>
</html>
```